Hello my Name is Ernesto Quiroga. I buy and sell vintage comic books, you can refer to my pictrogrid page kdrw.comics to get ideas and inspiration. For the front of the card I would like my company logo KDRW Comics with a yellow and black background with the owl beacon or bat emblem like on my PG page and with my info Ernesto Quiroga as the Owner and address/ phone number, PO Box 218739, Harbor Vale, FL 33090, 305-555-0182 and that I buy and sell comics & collectables . Also feel free to be open to other ideas if you want. Im not stuck on one design. For the back of the card I would like for it to say follow me on Pictogrid KDRW.Comics with the pg emblem. Also would like the card to be vertical if possible. Thanks

```html
<!DOCTYPE html>
<html lang="en">
<head>
<meta charset="utf-8">
<title>KDRW Comics – Business Card</title>
<link href="https://fonts.googleapis.com/css2?family=Audiowide&family=Roboto:wght@400;500&display=swap" rel="stylesheet">
<style>
  :root {
    --stage: #1b1d20;
    --yellow: #fcc817;
    --black: #0c0c0c;
    --white: #ffffff;
    --ink: #141414;
    --card-w: 340px;
    --card-h: 595px;
  }
  * { box-sizing: border-box; margin: 0; padding: 0; }
  html, body { width: 1200px; height: 987px; overflow: hidden; }
  body {
    background: var(--stage);
    display: flex;
    align-items: center;
    justify-content: center;
    gap: 90px;
    font-family: "Roboto", Arial, sans-serif;
  }
  .card {
    width: var(--card-w);
    height: var(--card-h);
    position: relative;
    overflow: hidden;
    box-shadow: 0 18px 40px rgba(0,0,0,.55);
  }

  /* Front */
  .card-front { background: var(--yellow); display: flex; flex-direction: column; }
  .front-top {
    height: 315px;
    background: var(--white);
    display: flex;
    align-items: center;
    justify-content: center;
  }
  .brand-tile {
    width: 205px;
    height: 205px;
    background: var(--yellow);
    display: flex;
    align-items: center;
    justify-content: center;
    text-align: center;
  }
  .brand-name {
    font-family: "Audiowide", "Arial Black", sans-serif;
    color: var(--black);
    line-height: 1.05;
  }
  .brand-tile .brand-name { font-size: 40px; }
  .name-band {
    height: 80px;
    background: var(--black);
    display: flex;
    flex-direction: column;
    align-items: center;
    justify-content: center;
    gap: 6px;
  }
  .owner-name {
    font-family: "Audiowide", "Arial Black", sans-serif;
    font-weight: 400;
    color: var(--yellow);
    font-size: 22px;
    letter-spacing: 1.5px;
    text-transform: uppercase;
  }
  .owner-title { color: var(--white); font-size: 13px; letter-spacing: .5px; }
  .contact {
    flex: 1;
    display: flex;
    flex-direction: column;
    align-items: center;
    justify-content: center;
    color: var(--ink);
    font-size: 15px;
    line-height: 1.3;
    text-align: center;
  }
  .address { margin-bottom: 14px; }
  .contact-line { display: flex; align-items: center; gap: 6px; }
  .contact-line svg { width: 12px; height: 12px; fill: var(--ink); flex: none; }

  /* Back */
  .card-back {
    background: var(--yellow);
    display: flex;
    flex-direction: column;
    align-items: center;
  }
  .tagline {
    margin-top: 110px;
    font-family: "Audiowide", "Arial Black", sans-serif;
    font-weight: 400;
    font-size: 19px;
    line-height: 1.3;
    letter-spacing: 1px;
    text-transform: uppercase;
    text-align: center;
    color: var(--black);
  }
  .back-brand {
    flex: 1;
    display: flex;
    align-items: center;
    justify-content: center;
    text-align: center;
  }
  .back-brand .brand-name { font-size: 56px; }
  .social-handle {
    margin-bottom: 92px;
    display: flex;
    align-items: center;
    gap: 6px;
    font-size: 17px;
    color: var(--black);
  }
  .handle-mark {
    width: 16px;
    height: 16px;
    border: 2px solid var(--black);
    border-radius: 3px;
  }
</style>
</head>
<body>

  <section class="card card-front" aria-label="Business card front">
    <div class="front-top">
      <div class="brand-tile">
        <span class="brand-name">KDRW<br>Comics</span>
      </div>
    </div>
    <div class="name-band">
      <h1 class="owner-name">Ernesto Quiroga</h1>
      <p class="owner-title">OWNER</p>
    </div>
    <div class="contact">
      <p class="address">PO Box 218739<br>Harbor Vale, FL 33090</p>
      <p class="contact-line">
        <svg viewBox="0 0 24 24" aria-hidden="true"><path d="M6.6 10.8a15.1 15.1 0 0 0 6.6 6.6l2.2-2.2c.3-.3.7-.4 1-.2 1.1.4 2.3.6 3.6.6.6 0 1 .4 1 1V20c0 .6-.4 1-1 1A17 17 0 0 1 3 4c0-.6.4-1 1-1h3.5c.6 0 1 .4 1 1 0 1.3.2 2.5.6 3.6.1.3 0 .7-.2 1z"/></svg>
        305-555-0182
      </p>
      <p class="contact-line">
        <svg viewBox="0 0 24 24" aria-hidden="true"><path d="M2 5h20v14H2z M4 7v.5l8 5 8-5V7l-8 5z" fill-rule="evenodd"/></svg>
        ernesto@kdrwcomics.com
      </p>
      <p class="contact-line">
        <svg viewBox="0 0 24 24" aria-hidden="true"><circle cx="12" cy="12" r="10"/></svg>
        www.kdrwcomics.com
      </p>
    </div>
  </section>

  <section class="card card-back" aria-label="Business card back">
    <h2 class="tagline">Buy &amp; Sell Comics<br>&amp; Collectables</h2>
    <div class="back-brand">
      <span class="brand-name">KDRW<br>Comics</span>
    </div>
    <p class="social-handle"><span class="handle-mark" aria-hidden="true"></span>KDRW.Comics</p>
  </section>

</body>
</html>
```